Custom Anatomical Healing Abutment Flyer

Need a Flyer (4x6 inch) color printed suffer for orders..
See attachment for what I'm looking for. just need it to look Nice (eye candy)...

- reduce the number of steps to 5 (pictures included)

you can remove the watermark (have approval from him to use this) just need to add "permission from lorvantic"

- Tag Line: (can change the wording if needed)
Custom Anatomical Healing Abutment
Available in Silicone and 3D printed

Target Market(s)

Letting customers know of new product available.

Font styles to use
Sans Serif

Colors

Designer to choose colors to be used in the design.

Requirements
Must have
• - reduce the number of steps to 5 (pictures included)
• you can remove the watermark (have approval from him to use this) just need to add "permission from lorvantic"
Nice to have
• - Tag Line: (can change the wording if needed)
• Custom Anatomical Healing Abutment
• Available in Silicone and 3D printed

```html
<!DOCTYPE html>
<html lang="en">
<head>
<meta charset="utf-8">
<title>Custom Anatomical Healing Abutment Flyer</title>
<link rel="stylesheet" href="https://fonts.googleapis.com/css2?family=Oswald:wght@500;700&family=Montserrat:wght@300;400&display=swap">
<style>
  :root {
    --navy-light: #3a3791;
    --navy-dark: #1c1950;
    --navy-ring: #2c2a7c;
    --headline-green: #8dc63f;
    --tagline-yellow: #f5c518;
    --white: #ffffff;
    --step-green: #1fa64a;
    --step-orange: #f59e1b;
    --step-yellow: #f2c40f;
    --step-lime: #8cc63f;
    --step-teal: #1ba4b8;
  }
  html, body { margin: 0; padding: 0; overflow: hidden; }
  body { width: 707px; height: 1200px; background: #ffffff; }
  .flyer {
    position: relative;
    width: 707px;
    height: 1200px;
    overflow: hidden;
    background: radial-gradient(ellipse at 50% 45%, var(--navy-light) 0%, #2a2672 45%, var(--navy-dark) 100%);
    font-family: "Montserrat", sans-serif;
  }
  .headline {
    position: absolute;
    top: 52px; left: 0; width: 100%;
    margin: 0;
    text-align: center;
    font-family: "Oswald", sans-serif;
    font-weight: 700;
    font-size: 68px;
    line-height: 1;
    letter-spacing: 0.5px;
    color: var(--headline-green);
  }
  .subhead {
    position: absolute;
    top: 134px; left: 0; width: 100%;
    margin: 0;
    text-align: center;
    font-family: "Montserrat", sans-serif;
    font-weight: 300;
    font-size: 34px;
    letter-spacing: 6px;
    color: var(--white);
  }
  .steps { position: absolute; top: 0; left: 0; }
  .step-number {
    font-family: "Montserrat", sans-serif;
    font-weight: 400;
    font-size: 22px;
    fill: #111111;
  }
  .availability {
    position: absolute;
    top: 990px; left: 0; width: 100%;
    margin: 0;
    text-align: center;
    font-family: "Oswald", sans-serif;
    font-weight: 700;
    font-size: 44px;
    line-height: 1;
    color: var(--tagline-yellow);
  }
  .printed {
    position: absolute;
    top: 1048px; left: 0; width: 100%;
    margin: 0;
    text-align: center;
    font-family: "Oswald", sans-serif;
    font-weight: 700;
    font-size: 84px;
    line-height: 1;
    letter-spacing: 2px;
    color: #f4f4f4;
    text-shadow: 1px 1px 0 #bdbdbd, 2px 2px 0 #9a9a9a, 3px 3px 0 #7a7a7a, 4px 4px 0 #5c5c5c, 6px 7px 8px rgba(0,0,0,0.55);
  }
  .permission {
    position: absolute;
    top: 1158px; left: 0; width: 100%;
    display: flex;
    align-items: center;
    justify-content: center;
    gap: 10px;
    font-family: "Montserrat", sans-serif;
    font-size: 12px;
    letter-spacing: 0.5px;
    color: var(--white);
    text-transform: uppercase;
  }
  .permission::before, .permission::after {
    content: "";
    width: 90px;
    height: 1px;
    background: linear-gradient(90deg, transparent, var(--white));
  }
  .permission::after { background: linear-gradient(90deg, var(--white), transparent); }
</style>
</head>
<body>
<main class="flyer">
  <h1 class="headline">CUSTOM ANATOMICAL</h1>
  <p class="subhead">HEALING ABUTMENT</p>

  <svg class="steps" width="707" height="1200" viewBox="0 0 707 1200" aria-label="Five step process around a happy couple">
    <defs>
      <radialGradient id="photo-lab" cx="50%" cy="40%" r="60%">
        <stop offset="0" stop-color="#6b7a86"/><stop offset="1" stop-color="#1d2a35"/>
      </radialGradient>
      <radialGradient id="photo-glove" cx="50%" cy="50%" r="60%">
        <stop offset="0" stop-color="#7fd1c8"/><stop offset="1" stop-color="#2a4a5a"/>
      </radialGradient>
      <radialGradient id="photo-cure" cx="45%" cy="45%" r="60%">
        <stop offset="0" stop-color="#5a4fc8"/><stop offset="1" stop-color="#1b2b4a"/>
      </radialGradient>
      <radialGradient id="photo-mouth" cx="50%" cy="50%" r="60%">
        <stop offset="0" stop-color="#e8c7c4"/><stop offset="1" stop-color="#a3525c"/>
      </radialGradient>
      <radialGradient id="photo-couple" cx="50%" cy="45%" r="60%">
        <stop offset="0" stop-color="#f3d6c2"/><stop offset="0.6" stop-color="#d3a88a"/><stop offset="1" stop-color="#eef3f4"/>
      </radialGradient>
    </defs>

    <g class="connectors" stroke-width="64" stroke-linecap="round">
      <line x1="353" y1="600" x2="353" y2="383" stroke="var(--step-green)"/>
      <line x1="353" y1="600" x2="578" y2="546" stroke="var(--step-orange)"/>
      <line x1="353" y1="600" x2="493" y2="794" stroke="var(--step-yellow)"/>
      <line x1="353" y1="600" x2="221" y2="809" stroke="var(--step-lime)"/>
      <line x1="353" y1="600" x2="136" y2="546" stroke="var(--step-teal)"/>
    </g>

    <g class="step-rings">
      <circle cx="353" cy="383" r="110" fill="var(--step-green)"/>
      <circle cx="578" cy="546" r="110" fill="var(--step-orange)"/>
      <circle cx="493" cy="794" r="110" fill="var(--step-yellow)"/>
      <circle cx="221" cy="809" r="110" fill="var(--step-lime)"/>
      <circle cx="136" cy="546" r="110" fill="var(--step-teal)"/>
    </g>

    <circle class="center-frame" cx="353" cy="600" r="142" fill="var(--navy-ring)"/>

    <circle cx="353" cy="600" r="126" fill="url(#photo-couple)" role="img" aria-label="Photo of a smiling senior couple"/>
    <circle cx="353" cy="383" r="92" fill="url(#photo-lab)" role="img" aria-label="Step 1: milling the abutment in a silicone mould"/>
    <circle cx="578" cy="546" r="92" fill="url(#photo-glove)" role="img" aria-label="Step 2: filling the mould with a gloved hand"/>
    <circle cx="493" cy="794" r="92" fill="url(#photo-cure)" role="img" aria-label="Step 3: light curing the abutment"/>
    <circle cx="221" cy="809" r="92" fill="url(#photo-mouth)" role="img" aria-label="Step 4: abutment seated in the mouth"/>
    <circle cx="136" cy="546" r="92" fill="url(#photo-mouth)" role="img" aria-label="Step 5: healed gum contour around the implant"/>

    <g class="step-badges" fill="var(--white)">
      <circle cx="283" cy="437" r="16"/>
      <circle cx="511" cy="484" r="16"/>
      <circle cx="521" cy="716" r="16"/>
      <circle cx="303" cy="806" r="16"/>
      <circle cx="172" cy="631" r="16"/>
    </g>
    <g class="step-number" text-anchor="middle">
      <text x="283" y="445">1</text>
      <text x="511" y="492">2</text>
      <text x="521" y="724">3</text>
      <text x="303" y="814">4</text>
      <text x="172" y="639">5</text>
    </g>
  </svg>

  <p class="availability">AVAILABLE IN SILICONE AND</p>
  <p class="printed">3D PRINTED</p>
  <div class="permission">Permission from lorvantic</div>
</main>
</body>
</html>
```